Bref créative
The Marlowe Gala
Event Planning
Professional
Rosalind Hartwell
Owner - The Marlowe Gala
4105 - 27 Ashcombe Avenue
Toronto, ON M5R 2K7
rosalind@TheMarloweGala.example
www.TheMarloweGala.example
The card can be single or double sided i don't mind. Just be creative and make it clean!!!
Thanks!
It can be single or double sided I dont mind.

```html
<!DOCTYPE html>
<html lang="en">
<head>
<meta charset="utf-8">
<title>The Marlowe Gala — Business Card</title>
<link rel="stylesheet" href="https://fonts.googleapis.com/css2?family=Raleway:wght@300;400;600&display=swap">
<style>
  :root {
    --bg: #ecebe8;
    --card: #ffffff;
    --ink: #3c3c3c;
    --ink-soft: #6d6d6d;
    --mark: #4a4a4a;
    --band-dark: #5e5e5e;
    --band-light: #bdbdbd;
    --rule: #c9c9c9;
  }
  * { box-sizing: border-box; margin: 0; padding: 0; }
  html, body { width: 1200px; height: 629px; overflow: hidden; }
  body {
    background: var(--bg);
    font-family: "Raleway", sans-serif;
    color: var(--ink);
    position: relative;
  }
  .card {
    position: absolute;
    top: 166px;
    width: 520px;
    height: 297px;
    background: var(--card);
    box-shadow: 0 2px 10px rgba(0,0,0,0.12);
    overflow: hidden;
  }
  .card--front { left: 50px; }
  .card--back { left: 630px; }

  .brand { display: flex; flex-direction: column; align-items: center; }
  .brand__square { width: 62px; height: 62px; background: var(--mark); margin-bottom: 12px; }
  .brand__name {
    font-weight: 400; font-size: 21px; letter-spacing: 2px;
    text-transform: uppercase; color: var(--ink); white-space: nowrap;
  }
  .brand__tagline {
    font-weight: 400; font-size: 8px; letter-spacing: 3px; text-transform: uppercase;
    color: var(--ink-soft); margin-top: 5px; padding-top: 4px; border-top: 1px solid var(--rule);
  }
  .card--front .brand { position: absolute; left: 0; right: 0; top: 78px; }

  .card--back .brand { position: absolute; left: 44px; top: 30px; }
  .card--back .brand__square { width: 50px; height: 50px; margin-bottom: 9px; }
  .card--back .brand__name { font-size: 16px; letter-spacing: 1.5px; }
  .card--back .brand__tagline { font-size: 6.5px; }

  .person { position: absolute; left: 44px; top: 140px; }
  .person__name { font-weight: 600; font-size: 11px; color: var(--ink); }
  .person__role { font-size: 8px; color: var(--ink-soft); margin-top: 3px; }
  .person__address { font-size: 8px; color: var(--ink-soft); margin-top: 10px; line-height: 1.5; font-style: normal; }

  .contacts { position: absolute; left: 300px; top: 46px; list-style: none; }
  .contacts li { display: flex; align-items: center; font-size: 8.5px; color: var(--ink); height: 19px; }
  .contacts .icon {
    width: 12px; height: 12px; border-radius: 50%; background: var(--mark);
    margin-right: 8px; display: flex; align-items: center; justify-content: center;
  }
  .contacts .icon svg { width: 7px; height: 7px; }

  .bands { position: absolute; left: 0; bottom: 0; width: 520px; height: 110px; }
</style>
</head>
<body>
  <section class="card card--front">
    <div class="brand">
      <div class="brand__square"></div>
      <div class="brand__name">The Marlowe Gala</div>
      <div class="brand__tagline">Event Planning</div>
    </div>
  </section>

  <section class="card card--back">
    <div class="brand">
      <div class="brand__square"></div>
      <div class="brand__name">The Marlowe Gala</div>
      <div class="brand__tagline">Event Planning</div>
    </div>

    <div class="person">
      <div class="person__name">Rosalind Hartwell</div>
      <div class="person__role">Owner - The Marlowe Gala</div>
      <address class="person__address">4105 - 27 Ashcombe Avenue<br>Toronto, ON M5R 2K7</address>
    </div>

    <ul class="contacts">
      <li><span class="icon"><svg viewBox="0 0 10 10"><path d="M2 1l2 2-1 1.2a6 6 0 0 0 2.8 2.8L7 6l2 2-1.3 1.3C4.5 9 1 5.5.7 2.3z" fill="#fff"/></svg></span>416.555.0142</li>
      <li><span class="icon"><svg viewBox="0 0 10 10"><rect x="3" y="1" width="4" height="8" rx="0.8" fill="#fff"/></svg></span>647.555.0198</li>
      <li><span class="icon"><svg viewBox="0 0 10 10"><rect x="1.5" y="3" width="7" height="5" fill="#fff"/><rect x="3" y="1" width="4" height="2" fill="#fff"/></svg></span>416.555.0176</li>
      <li><span class="icon"><svg viewBox="0 0 10 10"><rect x="1" y="2.5" width="8" height="5.5" fill="#fff"/><path d="M1 2.5l4 3 4-3" stroke="#4a4a4a" stroke-width="0.8" fill="none"/></svg></span>rosalind@TheMarloweGala.example</li>
      <li><span class="icon"><svg viewBox="0 0 10 10"><circle cx="5" cy="5" r="3.6" stroke="#fff" stroke-width="1" fill="none"/><path d="M1.4 5h7.2M5 1.4v7.2" stroke="#fff" stroke-width="0.8"/></svg></span>www.TheMarloweGala.example</li>
    </ul>

    <svg class="bands" viewBox="0 0 520 110" preserveAspectRatio="none" aria-hidden="true">
      <path d="M0 110 C160 92 340 70 520 12 L520 110 Z" fill="var(--band-light)"/>
      <path d="M60 110 C220 98 380 80 520 34 L520 110 Z" fill="var(--card)"/>
      <path d="M90 110 C250 100 400 84 520 44 L520 110 Z" fill="var(--band-dark)"/>
    </svg>
  </section>
</body>
</html>
```